KORVEL Company sign

We are building a new IT building and want to showcase that with a big sign on the block of land. We also want to utilize the sign and put it inside the office in the reception once it is built. We are a managed IT company and unique for the area we live. We have 18 staff and growing rapidly. We plan to be hear for a long time and providing jobs for the future. We want something catchy and that stands out and looks good. our target audience is corporate businesses and we highlight our level of responsiveness and care. Let me know if this is enough information to get started. It would be great to include that we are local supporting local.

Target Market(s)

Cooperate Businesses

```html
<!DOCTYPE html>
<html lang="en">
<head>
<meta charset="utf-8">
<title>KORVEL Company Sign</title>
<link rel="stylesheet" href="https://fonts.googleapis.com/css2?family=Oswald:wght@500;600&family=Open+Sans:wght@400;600;700;800&display=swap">
<style>
  :root {
    --bg: #404040;
    --white: #ffffff;
    --panel: #f3f4f6;
    --ink: #2b2b2b;
    --muted: #777c84;
    --blue: #2f6fd0;
    --blue-deep: #2a4fb0;
    --band: #4a4a4a;
    --band-dark: #2e2e2e;
  }
  * { margin: 0; padding: 0; box-sizing: border-box; }
  html, body { width: 960px; height: 1200px; overflow: hidden; }
  body { background: var(--bg); font-family: "Open Sans", Arial, sans-serif; position: relative; }

  .sign {
    position: absolute; left: 30px; top: 376px;
    width: 900px; height: 449px;
    background: linear-gradient(135deg, var(--white) 0%, var(--panel) 100%);
    overflow: hidden;
    box-shadow: 0 30px 40px rgba(0,0,0,0.35);
  }
  .sign-art { position: absolute; inset: 0; width: 900px; height: 449px; }

  .brand { position: absolute; left: 25px; top: 28px; display: flex; align-items: flex-start; gap: 12px; }
  .brand-mark { width: 84px; height: 84px; border-radius: 50%; background: var(--blue); flex: none; }
  .brand-text { padding-top: 4px; }
  .brand-name { font-weight: 700; font-size: 44px; line-height: 44px; color: var(--blue); letter-spacing: 2px; }
  .brand-tagline { font-size: 12px; letter-spacing: 3px; color: var(--muted); margin-top: 4px; white-space: nowrap; }
  .brand-services {
    margin-top: 3px; background: var(--blue); color: var(--white);
    font-size: 10.5px; border-radius: 8px; padding: 1px 10px; white-space: nowrap; display: inline-block;
  }

  .headline { position: absolute; left: 26px; top: 148px; }
  .headline-intro { font-size: 40px; line-height: 44px; color: var(--ink); font-weight: 400; }
  .headline-main {
    font-family: "Oswald", "Arial Narrow", sans-serif; font-weight: 600;
    font-size: 62px; line-height: 66px; color: var(--blue-deep); letter-spacing: 0.5px;
  }
  .headline-sub { font-size: 37px; line-height: 42px; font-weight: 800; color: var(--ink); letter-spacing: 1px; }

  .contact-phone {
    position: absolute; left: 0; top: 318px; width: 470px; height: 68px;
    background: linear-gradient(180deg, var(--band) 0%, var(--band-dark) 100%);
    display: flex; align-items: center; padding-left: 24px; gap: 14px;
    color: var(--white); font-weight: 700; font-size: 45px;
  }
  .icon-circle { width: 44px; height: 44px; border-radius: 50%; background: var(--white); display: flex; align-items: center; justify-content: center; flex: none; }
  .contact-web {
    position: absolute; left: 0; top: 392px; height: 52px;
    display: flex; align-items: center; padding-left: 24px; gap: 22px;
    font-size: 30px; color: var(--ink);
  }
  .icon-circle.dark { width: 38px; height: 38px; background: var(--band-dark); }
</style>
</head>
<body>
  <section class="sign">
    <svg class="sign-art" viewBox="0 0 900 449">
      <defs>
        <linearGradient id="photoFill" x1="0" y1="0" x2="0" y2="1">
          <stop offset="0" stop-color="#4e3f3e"/>
          <stop offset="0.6" stop-color="#6d5d5a"/>
          <stop offset="0.72" stop-color="#d9d6d3"/>
          <stop offset="1" stop-color="#ecebea"/>
        </linearGradient>
        <linearGradient id="swoop" x1="0" y1="0" x2="1" y2="1">
          <stop offset="0" stop-color="#2f86e0"/>
          <stop offset="1" stop-color="#2a3fa8"/>
        </linearGradient>
      </defs>
      <path d="M478 0 L560 0 C470 210 505 370 610 449 L588 449 C470 380 420 200 478 0 Z" fill="url(#swoop)"/>
      <path d="M560 0 L900 0 L900 449 L610 449 C505 370 470 210 560 0 Z" fill="url(#photoFill)" role="img" aria-label="Photo of two young children in company t-shirts sitting on the floor with a telephone, headset and laptop"/>
      <path d="M610 449 C505 370 470 210 560 0" fill="none" stroke="#ffffff" stroke-width="4"/>
    </svg>

    <div class="brand">
      <div class="brand-mark"></div>
      <div class="brand-text">
        <div class="brand-name">KORVEL</div>
        <div class="brand-tagline">LOCAL CARE. FAST RESPONSE</div>
        <div class="brand-services">1300 555 018 • CORPORATE I.T. SERVICES</div>
      </div>
    </div>

    <div class="headline">
      <div class="headline-intro">WE ARE</div>
      <div class="headline-main">PROVIDING JOBS</div>
      <div class="headline-sub">FOR THE FUTURE</div>
    </div>

    <div class="contact-phone">
      <span class="icon-circle">
        <svg width="26" height="26" viewBox="0 0 24 24"><path d="M6.6 10.8a15.1 15.1 0 0 0 6.6 6.6l2.2-2.2a1 1 0 0 1 1-.25 11.4 11.4 0 0 0 3.6.57 1 1 0 0 1 1 1V20a1 1 0 0 1-1 1A17 17 0 0 1 3 4a1 1 0 0 1 1-1h3.5a1 1 0 0 1 1 1c0 1.25.2 2.45.57 3.57a1 1 0 0 1-.25 1z" fill="#2e2e2e"/></svg>
      </span>
      <span class="phone-number">1300-555-018</span>
    </div>

    <div class="contact-web">
      <span class="icon-circle dark">
        <svg width="22" height="22" viewBox="0 0 24 24" fill="none" stroke="#ffffff" stroke-width="1.6"><circle cx="12" cy="12" r="9"/><ellipse cx="12" cy="12" rx="4" ry="9"/><path d="M3 12h18M5 7h14M5 17h14"/></svg>
      </span>
      <span class="web-address">www.korvel.com.au</span>
    </div>
  </section>
</body>
</html>
```